Recruitment website home page design

I'm looking for designs for a recruitment services website home page.

The key message for this website is that we will find the right candidate for the recruiter fast in a market where they have to trawl through many, many unsuitable CVs to reach the small handful of candidates that are of real interest to them. The design should feel light, modern, clear - much like the taskorbit site feels.

Your submission should be a home page design. The page should include a login box, obvious link to sign-up (a 30 day free trial is available) and content communicating the key selling points of the service. Please use the taskorbit logo in your design (the real one is also blue). Note that this is not a contest to design a recruitment system, this is about the design of the key page to position the brand and quality to the visitor.

This project is for a market test by a leading UK organisation. If successful this could lead to considerable follow on work and a very good name to add to your portfolio. Your submission should be original content and copyright of the chosen work would be transferred to the organisation I represent on payment of the contest prize to the winning designer.

Good luck!

```html
<!DOCTYPE html>
<html lang="en">
<head>
<meta charset="utf-8">
<title>Recruitment Services – Home</title>
<link href="https://fonts.googleapis.com/css2?family=PT+Sans:wght@400;700&display=swap" rel="stylesheet">
<style>
:root{
  --lime:#a8cc00;
  --lime-dark:#7f9c00;
  --lime-text:#8cb000;
  --ink:#555;
  --ink-soft:#666;
  --slate:#666666;
  --bar:#444444;
  --white:#ffffff;
  --sky-a:#9fb9d2;
  --sky-b:#5f83a8;
}
*{box-sizing:border-box;margin:0;padding:0}
html,body{width:837px;height:1200px;overflow:hidden}
body{font-family:"PT Sans",sans-serif;color:var(--ink)}
.page{position:relative;width:837px;height:1200px;overflow:hidden;
  background:linear-gradient(#ededed 0,#d6d6d6 333px,#5c5c5c 333px,#7a7a7a 520px,#b0b0b0 800px,#d4d4d4 1000px,#e2e2e2 1200px)}
.abs{position:absolute}

/* header ribbon */
.masthead{left:84px;top:17px;width:668px;height:37px;background:var(--lime)}
.masthead::before,.masthead::after{content:"";position:absolute;bottom:-9px;border-top:9px solid var(--lime-dark)}
.masthead::before{left:0;border-left:7px solid transparent}
.masthead::after{right:0;border-right:7px solid transparent}
.brand{position:absolute;left:24px;top:4px;font-size:23px;font-weight:700;color:var(--white);letter-spacing:-.3px}
.social{position:absolute;right:26px;top:11px;display:flex;gap:4px}
.social span{width:17px;height:17px;border-radius:2px;background:rgba(255,255,255,.75)}

/* hero panel */
.hero-panel{left:90px;top:54px;width:652px;height:342px;background:var(--white)}
.hero-photo{left:108px;top:68px;width:417px;height:283px;background:linear-gradient(120deg,var(--sky-a),#c6d4e3 45%,var(--sky-b))}
.trial{left:525px;top:68px;width:203px;height:135px;background:var(--slate);text-align:center;color:var(--white)}
.trial::after{content:"";position:absolute;left:96px;bottom:-8px;border:8px solid transparent;border-top-color:var(--slate);border-bottom:0}
.trial .lime{color:var(--lime);font-size:23px;line-height:1}
.trial .t1{margin-top:26px}
.trial .big{font-size:31px;line-height:1;margin:7px 0 5px}
.login{left:525px;top:203px;width:203px;height:148px;background:var(--lime);padding:20px 14px 0}
.login label{display:block;font-size:11px;color:#3d3d3d;margin-bottom:3px}
.login .field{height:24px;background:var(--white);border:1px solid #8aa800;margin-bottom:14px}
.login .signin{position:absolute;right:10px;bottom:18px;background:var(--bar);color:var(--white);font-size:11px;font-weight:700;padding:3px 9px}
.steps{left:108px;top:351px;width:620px;height:30px;background:var(--bar);display:flex}
.steps div{flex:1;color:var(--white);font-size:11px;font-weight:700;text-align:center;line-height:30px;border-left:1px solid #5a5a5a}
.steps div:first-child{border-left:0;color:var(--lime)}
.steps b{font-size:16px;margin-right:3px}

/* info panel */
.info-panel{left:95px;top:405px;width:647px;height:265px;background:var(--white)}
.rule{height:8px;background:var(--lime)}
h2.section{font-size:18px;font-weight:400;color:var(--lime-text);border-bottom:1px solid #ccc;padding-bottom:2px}
.bullets{list-style:none;font-size:10px;color:var(--ink-soft)}
.bullets li{position:relative;padding-left:14px}
.bullets li::before{content:"";position:absolute;left:1px;top:3px;width:7px;height:7px;background:var(--lime-text)}
.para{font-size:9.4px;line-height:11.5px;color:var(--ink-soft)}
.btn{display:inline-block;background:var(--slate);color:var(--white);font-size:12px;padding:2px 7px}

/* cards */
.card{width:182px;height:312px;background:var(--white);border-top:8px solid var(--lime)}
.card .photo{height:149px}
.card h3{margin:9px 16px 0;font-size:17px;font-weight:400;color:var(--lime-text);border-bottom:1px solid #ccc;letter-spacing:.5px}
.card .para{margin:5px 16px 0;font-size:8.6px;line-height:11px}
.card .btn{position:absolute;left:16px;bottom:11px}

/* footer */
.foot-rule{left:95px;top:1013px;width:647px;height:3px;background:var(--lime-dark)}
.foot-col{top:1026px;width:143px}
.foot-col h4{font-size:12px;font-weight:400;color:var(--ink);letter-spacing:.3px;border-bottom:1px solid var(--lime);padding-bottom:1px;margin-bottom:6px}
.foot-col ul{list-style:none;font-size:9.4px;color:var(--ink-soft)}
.foot-col li{height:16px;padding-left:13px;position:relative}
.foot-col li::before{content:"";position:absolute;left:0;top:3px;width:8px;height:8px;background:#888;clip-path:polygon(0 0,100% 50%,0 100%)}
.contact{font-size:9.4px;line-height:13px;color:var(--ink-soft)}
.subscribe p{font-size:11px;line-height:13px;color:var(--lime-text)}
.sub-field{left:589px;top:1105px;width:143px;height:18px;background:var(--white);border:1px solid #ccc}
.sub-btn{left:674px;top:1129px;width:58px;height:19px;background:var(--lime-dark);color:var(--white);font-size:10px;line-height:19px;text-align:center}
.bottom-rule{left:95px;top:1160px;width:647px;height:3px;background:#999}
.legal{left:93px;top:1171px;font-size:8.4px;line-height:12px;color:var(--ink)}
.follow{left:608px;top:1170px;height:20px;border-left:1px solid #999;padding-left:6px;display:flex;align-items:center;gap:4px;font-size:10px;color:var(--ink);letter-spacing:.5px}
.follow span{width:15px;height:15px;border-radius:50%;background:#666}
</style>
</head>
<body>
<div class="page">

  <header class="abs masthead">
    <div class="brand">RECRUITMENT SERVICES</div>
    <div class="social" aria-label="Social links"><span></span><span></span><span></span><span></span></div>
  </header>

  <section class="abs hero-panel"></section>
  <div class="abs hero-photo" role="img" aria-label="Photo of a professional touching a network of candidate icons"></div>
  <div class="abs trial">
    <div class="lime t1">A 30 DAY</div>
    <div class="big">FREE TRIAL</div>
    <div class="lime">IS AVAILABLE</div>
  </div>
  <form class="abs login">
    <label>User Name:</label><div class="field"></div>
    <label>Password:</label><div class="field"></div>
    <span class="signin">SIGN IN</span>
  </form>
  <nav class="abs steps">
    <div><b>1.</b>APPLICATION TYPE</div>
    <div><b>2.</b>YOUR DETAILS</div>
    <div><b>3.</b>PAYMENT</div>
    <div><b>4.</b>CONFIRMATION</div>
  </nav>

  <section class="abs info-panel"></section>
  <div class="abs rule" style="left:108px;top:418px;width:321px"></div>
  <div class="abs rule" style="left:432px;top:418px;width:297px"></div>

  <div class="abs" style="left:108px;top:435px;width:216px">
    <h2 class="section">What do you need us for?</h2>
  </div>
  <ul class="abs bullets" style="left:108px;top:462px;width:320px;line-height:15.7px">
    <li>Apply for your first provisional driving licence</li>
    <li>Change the address, name or photo on your DL</li>
    <li>Replace a lost, stolen, damaged or destroyed DL</li>
    <li>Renew or exchange your driving licence</li>
    <li>Remove expired endorsement (points)details</li>
  </ul>
  <span class="abs btn" style="left:107px;top:551px">Apply now »</span>
  <p class="abs para" style="left:108px;top:584px;width:320px">Lorem ipsum dolor sit amet, consectetuer adipiscing elit, sed diam nonummy nibh euismod tincidunt ut laoreet dolore magna aliquam erat volutpat. Ut wisi enim ad minim veniam, quis nostrud exerci tation ullamcorper suscipit lobortis nisl ut aliquip ex ea commodo consequat.</p>
  <span class="abs btn" style="left:330px;top:638px">Application »</span>

  <div class="abs" style="left:430px;top:435px;width:256px">
    <h2 class="section">Our Services:</h2>
  </div>
  <ul class="abs bullets" style="left:432px;top:462px;width:300px;line-height:11.3px">
    <li>Lorem ipsum dolor sit amet, consectetuer adipiscing elit</li>
    <li>Lorem ipsum dolor sit amet, consectetuer adipiscing elit</li>
    <li>Lorem ipsum dolor sit amet, consectetuer adipiscing elit</li>
    <li>Lorem ipsum dolor sit amet, consectetuer adipiscing elit</li>
  </ul>
  <p class="abs para" style="left:432px;top:522px;width:298px">Lorem ipsum dolor sit amet, consectetuer adipiscing elit, sed diam nonummy nibh euismod tincidunt ut laoreet dolore magna aliquam erat volutpat. Ut wisi enim ad minim veniam, quis nostrud exerci tation ullamcorper suscipit lobortis nisl ut aliquip ex ea commodo consequat.</p>
  <p class="abs para" style="left:432px;top:589px;width:298px">Lorem ipsum dolor sit amet, consectetuer adipiscing elit, sed diam nonummy nibh euismod tincidunt ut laoreet dolore magna aliquam erat volutpat. Ut wisi enim ad minim veniam, quis nostrud exerci tation ullamcorper suscipit lobortis nisl ut aliquip ex ea commodo consequat.</p>

  <article class="abs card" style="left:121px;top:684px">
    <div class="photo" role="img" aria-label="Photo of a support agent wearing a headset" style="background:linear-gradient(135deg,#1f3f8a,#3a5fae 60%,#d9d9d9)"></div>
    <h3>CAPTION</h3>
    <p class="para">Lorem ipsum dolor sit amet, consectetuer adipiscing elit, sed diam nonummy nibh euismod tincidunt ut laoreet dolore magna aliquam erat volutpat. Ut wisi enim ad minim veniam, quis nostrud exerci tation ullamcorper suscipit lobortis nisl ut aliquip ex ea commodo consequat.</p>
    <span class="btn">Read all »</span>
  </article>
  <article class="abs card" style="left:333px;top:684px">
    <div class="photo" role="img" aria-label="Photo of smiling colleagues in business attire" style="background:linear-gradient(135deg,#c9d3dc,#6f7d8c 55%,#2a3240)"></div>
    <h3>CAPTION</h3>
    <p class="para">Lorem ipsum dolor sit amet, consectetuer adipiscing elit, sed diam nonummy nibh euismod tincidunt ut laoreet dolore magna aliquam erat volutpat. Ut wisi enim ad minim veniam, quis nostrud exerci tation ullamcorper suscipit lobortis nisl ut aliquip ex ea commodo consequat.</p>
    <span class="btn">Read all »</span>
  </article>
  <article class="abs card" style="left:546px;top:684px">
    <div class="photo" role="img" aria-label="Photo of a hand passing a CV across a desk" style="background:linear-gradient(135deg,#3a3a3a,#cfcfcf 45%,#f2f2f2)"></div>
    <h3>CAPTION</h3>
    <p class="para">Lorem ipsum dolor sit amet, consectetuer adipiscing elit, sed diam nonummy nibh euismod tincidunt ut laoreet dolore magna aliquam erat volutpat. Ut wisi enim ad minim veniam, quis nostrud exerci tation ullamcorper suscipit lobortis nisl ut aliquip ex ea commodo consequat.</p>
    <span class="btn">Read all »</span>
  </article>

  <div class="abs foot-rule"></div>
  <div class="abs foot-col" style="left:96px">
    <h4>APPLICATION TYPE</h4>
    <ul><li>Lorem ipsum dolor</li><li>Lorem ipsum dolor</li><li>Lorem ipsum dolor</li><li>Lorem ipsum dolor</li><li>Lorem ipsum dolor</li><li>Lorem ipsum dolor</li></ul>
  </div>
  <div class="abs foot-col" style="left:257px">
    <h4>OUR SERVICES</h4>
    <ul><li>Lorem ipsum dolor</li><li>Lorem ipsum dolor</li><li>Lorem ipsum dolor</li><li>Lorem ipsum dolor</li><li>Lorem ipsum dolor</li><li>Lorem ipsum dolor</li></ul>
  </div>
  <div class="abs foot-col" style="left:422px">
    <h4>CONTACTS</h4>
    <p class="contact">Suite 12, Maple Court<br>210 Harbor Lane<br>USA, MD 20900<br>Toll Free: 000-555-0142<br>Fax: 000-555-0143</p>
  </div>
  <div class="abs foot-col subscribe" style="left:589px">
    <h4>SUBSCRIBE NOW!</h4>
    <p>Join our email list f for a Recruitment Services and offers.</p>
  </div>
  <div class="abs sub-field"></div>
  <div class="abs sub-btn">Subcribe »</div>

  <div class="abs bottom-rule"></div>
  <p class="abs legal">Home | About us | Services| Support | Contact us<br>Copyright © 2013 Recruitment Services. All rights reserved.</p>
  <div class="abs follow">FOLLOW US <span></span><span></span><span></span><span></span></div>

</div>
</body>
</html>
```